Gelato Business Card

create a new business card using existing logo

Target Market(s)

B2B

Contact Information for Business Card

typical contact info: logo, address, email, phone, rep name

Colors
0355a3
33a6d7

Requirements
Must have
• a feel of high quality, luxury, happiness
• use cool, comforting color and texture of business card.
Nice to have
• "A Little Perfection Goes A Long Way!" TM
• or, "more quality, more flavor"
• or, "Flavor Matters"

```html
<!DOCTYPE html>
<html lang="en">
<head>
<meta charset="UTF-8">
<title>Brunella's Gelato – Business Card</title>
<link rel="stylesheet" href="https://fonts.googleapis.com/css2?family=Questrial&family=Lato:wght@400;700&family=Dancing+Script:wght@500&display=swap">
<style>
  :root {
    --backdrop: #d6d6d6;
    --card-white: #ffffff;
    --brand-indigo: #3e4699;
    --name-indigo: #383f9c;
    --accent-sky: #2f9fd8;
    --text-dark: #2a2a2a;
    --rule-grey: #9a9a9a;
  }
  * { margin: 0; padding: 0; box-sizing: border-box; }
  html, body {
    width: 900px;
    height: 1200px;
    overflow: hidden;
    background: var(--backdrop);
  }
  .canvas {
    position: relative;
    width: 900px;
    height: 1200px;
  }
  .card {
    position: absolute;
    left: 86px;
    width: 734px;
    height: 429px;
    border-radius: 22px;
    overflow: hidden;
  }
  .card--front { top: 137px; background: var(--card-white); }
  .card--back  { top: 633px; background: var(--brand-indigo); }

  .brand-name {
    position: absolute;
    font-family: "Lato", sans-serif;
    font-weight: 700;
    letter-spacing: 1px;
    white-space: nowrap;
    display: flex;
    align-items: center;
    justify-content: center;
    gap: 10px;
  }
  .brand-dot {
    width: 16px;
    height: 16px;
    border-radius: 50%;
  }
  .card--front .brand-name {
    left: 344px;
    width: 345px;
    top: 104px;
    font-size: 28px;
    color: var(--brand-indigo);
  }
  .card--front .brand-dot { background: var(--brand-indigo); }
  .card--back .brand-name {
    left: 0;
    right: 0;
    top: 188px;
    font-size: 46px;
    gap: 12px;
    color: var(--card-white);
  }
  .card--back .brand-dot { background: var(--card-white); width: 22px; height: 22px; }

  .rep-name {
    position: absolute;
    left: 44px;
    top: 254px;
    font-family: "Questrial", sans-serif;
    font-weight: 700;
    font-size: 25px;
    color: var(--name-indigo);
    -webkit-text-stroke: 0.4px var(--name-indigo);
  }
  .rep-title {
    position: absolute;
    left: 44px;
    top: 287px;
    font-family: "Questrial", sans-serif;
    font-size: 17px;
    color: var(--accent-sky);
  }
  .title-rule {
    position: absolute;
    left: 177px;
    top: 301px;
    width: 512px;
    height: 1px;
    background: var(--rule-grey);
  }
  .contact-list {
    position: absolute;
    left: 44px;
    top: 316px;
    list-style: none;
    font-family: "Lato", sans-serif;
    font-size: 16px;
    color: var(--text-dark);
  }
  .contact-list li {
    display: flex;
    align-items: center;
    gap: 10px;
    height: 26px;
  }
  .contact-list svg { width: 16px; height: 16px; fill: var(--accent-sky); }
  .address {
    position: absolute;
    right: 45px;
    top: 316px;
    font-family: "Lato", sans-serif;
    font-style: normal;
    font-size: 16px;
    line-height: 26px;
    text-align: right;
    color: var(--text-dark);
  }
  .tagline {
    position: absolute;
    left: 0;
    right: 0;
    top: 354px;
    text-align: center;
    font-family: "Dancing Script", cursive;
    font-weight: 500;
    font-size: 30px;
    color: var(--card-white);
  }
</style>
</head>
<body>
<main class="canvas">

  <section class="card card--front" aria-label="Business card front">
    <div class="brand-name"><span class="brand-dot"></span>BRUNELLA'S GELATO</div>

    <h1 class="rep-name">Marcus Ellery</h1>
    <p class="rep-title">CEO/Founder</p>
    <div class="title-rule"></div>

    <ul class="contact-list">
      <li>
        <svg viewBox="0 0 24 24" aria-hidden="true"><path d="M6.6 10.8a15.1 15.1 0 0 0 6.6 6.6l2.2-2.2a1 1 0 0 1 1-.25 11.4 11.4 0 0 0 3.6.57 1 1 0 0 1 1 1V20a1 1 0 0 1-1 1A17 17 0 0 1 3 4a1 1 0 0 1 1-1h3.5a1 1 0 0 1 1 1c0 1.250.2 2.450.57 3.6a1 1 0 0 1-.25 1z"/></svg>
        <span>214-555-0148</span>
      </li>
      <li>
        <svg viewBox="0 0 24 24" aria-hidden="true"><path d="M2 5h20v14H2z M3.5 6.5v.4l8.5 6 8.5-6v-.4z" fill-rule="evenodd"/></svg>
        <span>marcus@brunellagelato.com</span>
      </li>
    </ul>

    <address class="address">
      118 Harbor Street NE<br>
      Suite 210, Lakeview<br>
      MI 49010
    </address>
  </section>

  <section class="card card--back" aria-label="Business card back">
    <div class="brand-name"><span class="brand-dot"></span>BRUNELLA'S GELATO</div>
    <p class="tagline">Every Scoop Is Made With Pure Joy!</p>
  </section>

</main>
</body>
</html>
```